依頼詳細
芳醇な味と香りの柚子果汁をアピールしたいと考えています。
ヨーロッパ圏の方に受けるデザインを希望します。
販売価格が高額になるため、高級感があり、モダンでスタイリッシュな雰囲気が理想。

■ラベルデザイン作成に関して
・高級感がある。漠然と、黒系がいいかなと思っております。
・色々な商品の中で埋もれない存在感も必要
・ターゲットは、現地富裕層・現地日本人・現地料理人等
・販売店舗は、現地のデパートや日本食関連の食材店等

◆必ず入れていただきたい文字等
1、ゆずの絵又は画像
2、搾り柚子(漢字で。大サイズ)
3、YUZU(中サイズ)
4、100% PURE(小サイズ)

※「搾り柚子」と「YUZU」のサイズは入れ替わっても構いません。

◆容量と瓶サイズ
・容量:200ml
・瓶高さ210㎜、底直径55㎜
・瓶は添付画像の通り(緑の瓶に黒フタ)

ご不明な点がございましたらお気軽にご連絡ください。
記載項目
★ラベルサイズ
縦H65mm×横W130mm(実質のデザイン部分は縦H65mm×横W54mm)
※デザインを決定後に各種表示箇所をお願いしたいと思います。

印刷/4色まで
*機械貼りになります。
希望イメージ
シンプル 複雑
単色 カラフル
暗い 明るい
日常 高級
遊び心 厳粛
未来的 伝統的
女性的 男性的
希望する色
茶系、グレー系
納品ファイル
• イラストレーター形式 (.ai)
補足説明
追記です。
こちらの商品は、柚子果汁00%の柑橘酢です。
甘味は全く入っておりません。
ジュースのように、そのまま飲んでいただくものでもありません。
レモン果汁のように、お料理にお使いいただいたり、ドリンクの材料にしていただいたり・・・です。
柑橘のお酢とお考え下さい。

▼日本国内でご提案しているお召し上がり方です▼
<<美味しいお召し上がり方>>
・醤油やだしを加えて自家製ぽん酢の材料に。
・自家製ドレッシングの材料に。
・焼酎にお好みで割って、爽やかな焼酎やカクテルに。
・蜂蜜やシロップを加えて、水・お湯または炭酸水やサイダーで割って、体が喜ぶ健康ドリンクに。

どうぞ、よろしくお願いいたします。
■ 選んだ理由

ヨーロッパ向けということで、オシャレな雰囲気のこちらに決めさせていただきました。柚子の玉を一筆描きで表現しているところが気に入りました。

■ 提案者全員のお礼・コメント

この度も、たくさんの方に提案を頂き心から感謝を申し上げます。
選定には大変迷いましたが、ステキな作品をたくさん目にすることができ、本当に良かったです。
またこちらでお願いする事があると思います。
今後ともどうぞよろしくお願いたします。

皆様の今後の活躍を心より祈願いたします。

```html
<!DOCTYPE html>
<html lang="ja">
<head>
<meta charset="utf-8">
<title>搾り柚子 YUZU 100% PURE — Label</title>
<link rel="stylesheet" href="https://fonts.googleapis.com/css2?family=Cinzel:wght@600&family=Playfair+Display:ital,wght@1,600&family=Shippori+Mincho:wght@800&family=Lato:wght@700;900&display=swap">
<style>
  :root {
    --canvas-bg: #f4f3ef;
    --label-green: #0f3a25;
    --label-green-deep: #0a2b1b;
    --gold: #c9a650;
    --gold-light: #e6cf86;
    --white: #ffffff;
    --yuzu-light: #fbeeb0;
    --yuzu: #f2cf3c;
    --yuzu-deep: #e0a81c;
    --leaf: #3f7a2e;
  }
  * { margin: 0; padding: 0; box-sizing: border-box; }
  html, body {
    width: 1200px;
    height: 2880px;
    overflow: hidden;
    background: var(--canvas-bg);
  }
  .canvas {
    position: relative;
    width: 1200px;
    height: 2880px;
  }
  .label {
    position: absolute;
    left: 100px;
    top: 957px;
    width: 1000px;
    height: 966px;
    overflow: hidden;
    background: radial-gradient(ellipse at 55% 40%, var(--label-green) 0%, var(--label-green-deep) 100%);
  }
  .label__band {
    position: absolute;
    left: 0;
    width: 100%;
    height: 16px;
    background: linear-gradient(90deg, var(--gold) 0%, var(--gold-light) 50%, var(--gold) 100%);
    z-index: 3;
  }
  .label__band--top { top: 0; }
  .label__band--bottom { bottom: 0; }
  .yuzu-slice {
    position: absolute;
    left: 228px;
    top: 16px;
    width: 572px;
    height: 200px;
  }
  .product-name-jp {
    position: absolute;
    left: 78px;
    top: 190px;
    writing-mode: vertical-rl;
    font-family: "Shippori Mincho", serif;
    font-weight: 800;
    font-size: 160px;
    line-height: 1;
    letter-spacing: 14px;
    color: var(--white);
    z-index: 2;
  }
  .product-info {
    position: absolute;
    left: 313px;
    top: 250px;
    width: 571px;
    text-align: center;
    z-index: 2;
  }
  .product-name {
    font-family: "Cinzel", serif;
    font-weight: 600;
    font-size: 196px;
    line-height: 1;
    letter-spacing: 10px;
    color: var(--gold);
  }
  .purity {
    margin-top: 14px;
    font-family: "Playfair Display", serif;
    font-style: italic;
    font-weight: 600;
    font-size: 104px;
    line-height: 1.05;
    color: var(--gold);
  }
  .category {
    margin-top: 20px;
    background: var(--white);
    color: var(--label-green);
    font-family: "Lato", sans-serif;
    font-weight: 900;
    font-size: 48px;
    line-height: 68px;
    letter-spacing: 2px;
  }
  .origin {
    margin-top: 20px;
    font-family: "Lato", sans-serif;
    font-weight: 700;
    font-size: 31px;
    letter-spacing: 1px;
    color: var(--white);
  }
  .yuzu-fruit {
    position: absolute;
    left: 200px;
    top: 700px;
    width: 560px;
    height: 250px;
    z-index: 1;
  }
</style>
</head>
<body>
<div class="canvas">
  <section class="label">
    <div class="label__band label__band--top"></div>

    <svg class="yuzu-slice" role="img" aria-label="Illustration of a halved yuzu slice" viewBox="0 0 572 200">
      <defs>
        <radialGradient id="sliceFill" cx="50%" cy="0%" r="100%">
          <stop offset="0%" stop-color="#fbeeb0"/>
          <stop offset="80%" stop-color="#f2cf3c"/>
          <stop offset="100%" stop-color="#e0a81c"/>
        </radialGradient>
      </defs>
      <path d="M0 0 A286 200 0 0 0 572 0 Z" fill="url(#sliceFill)"/>
    </svg>

    <h1 class="product-name-jp">搾り柚子</h1>

    <div class="product-info">
      <p class="product-name">YUZU</p>
      <p class="purity">100% PURE</p>
      <p class="category">CITRUS SEASONING</p>
      <p class="origin">MADE IN JAPAN,YAMAGUCHI</p>
    </div>

    <svg class="yuzu-fruit" role="img" aria-label="Illustration of a whole yuzu fruit with a green leaf" viewBox="0 0 560 250">
      <defs>
        <radialGradient id="fruitFill" cx="55%" cy="35%" r="70%">
          <stop offset="0%" stop-color="#fbeeb0"/>
          <stop offset="60%" stop-color="#f2cf3c"/>
          <stop offset="100%" stop-color="#e0a81c"/>
        </radialGradient>
      </defs>
      <circle cx="330" cy="240" r="230" fill="url(#fruitFill)"/>
    </svg>

    <div class="label__band label__band--bottom"></div>
  </section>
</div>
</body>
</html>
```